Lumen 7 auto detail

Looking for a flyer for my auto detail business
Hand Wash
• Clay Bar Application
• Machine Buff Wax / Compound /
Polish Paint Correction
• Clean Interior & Exterior Glass
• Vacuum, Shampoo, & Steam Clean
Upholstery, Carpets, Seats, Mats, & Trunk
• Pet Hair Removal
• Clean headliner
• Clean Doors/ Trunk/Hood Jambs
• Air Blow & Clean all Cracks & Crevices • Clean & Shine Protect All Vinyl/
Dash/Door Panels/Middle Console
Cleaning/Conditioning of Leather
• Clean, Treat, Dress, & Polish Tires,
Rims, & Wheel Wells
• Bug & Tar Removal
• Dress Black Exterior Plastic
• Minor Scratch Removal
• Engine Compartment Detail
Headlight Restoration (if needed)
• Interior Fragrance
• DRY ICE BLASTING
At Lumen 7 Auto Detail, we pride ourselves on providing a unique and exceptional experience that sets us apart from other detailers. Here are a few key factors that make us stand out:
1. Attention to Detail: We live up to our name by going above and beyond in every aspect of our car detailing services. Our team of skilled technicians pays meticulous attention to every nook and cranny of your vehicle, ensuring that it receives the highest level of care and precision.
2. Customized Solutions: We understand that each car is unique, and so are our clients' needs. That's why we offer personalized solutions tailored to your specific requirements. Whether you need a basic wash and wax or a comprehensive paint correction, we will work with you to create a customized detailing plan that meets your expectations.
3. Cutting-Edge Technology: We stay at the forefront of the industry by utilizing the latest tools, products, and techniques. Our team is trained in the most advanced detailing methods, allowing us to achieve superior results and deliver a finish that exceeds your expectations.
4. Exceptional Customer Service: We believe in providing not only exceptional car detailing but also an exceptional customer experience. Our friendly and knowledgeable staff is always ready to assist you, answer your questions, and ensure that you have a positive and enjoyable experience at our facility.
5. Eco-Friendly Practices: We are committed to reducing our environmental impact by using eco-friendly cleaning products and techniques. Our detailing processes are designed to minimize water usage and waste generation, making us a responsible choice for those who care about the planet.
These factors, combined with our passion for cars and dedication to excellence, make Lumen 7 Auto Detail the premier choice for discerning car owners who seek a truly exceptional detailing experience.
We offer mobile services as well
Address 742 Corliss Ave. S., Renton, WA 98061

```html
<!DOCTYPE html>
<html lang="en">
<head>
<meta charset="utf-8">
<title>Lumen 7 Auto Detail – Flyer</title>
<link rel="stylesheet" href="https://fonts.googleapis.com/css2?family=Kanit:ital,wght@1,700;1,800&family=Montserrat:wght@400;500&family=Oswald:wght@500;700&family=Roboto:wght@400&family=Russo+One&family=Mr+Dafoe&display=swap">
<style>
  :root {
    --black: #000000;
    --red: #e01010;
    --red-deep: #8a0000;
    --red-bright: #ff2a1a;
    --silver: #d9d9d9;
    --silver-dark: #8c8c8c;
    --white: #ffffff;
    --ink: #151515;
    --backdrop: #b4b4b4;
  }
  * { box-sizing: border-box; margin: 0; padding: 0; }
  html, body { width: 920px; height: 1200px; overflow: hidden; background: var(--backdrop); }
  .flyer {
    position: relative; width: 920px; height: 1200px; overflow: hidden;
    background: var(--black); color: var(--white);
    font-family: "Montserrat", sans-serif;
  }
  .abs { position: absolute; }

  /* Brand mark area */
  .brand { left: 60px; top: 40px; width: 290px; height: 200px; display: flex; align-items: center; justify-content: center; gap: 12px; }
  .brand-dot { width: 22px; height: 22px; border-radius: 50%; background: var(--red); flex: none; }
  .brand-name { font-family: "Montserrat", sans-serif; font-weight: 500; font-size: 26px; color: var(--white); white-space: nowrap; }

  /* Hero photo */
  .hero-rings { left: 0; top: 0; width: 920px; height: 520px; }

  /* Headline */
  .kicker { left: 103px; top: 280px; font-family: "Montserrat", sans-serif; font-weight: 500; font-size: 21px; letter-spacing: 6px; }
  .headline {
    font-family: "Russo One", sans-serif; font-size: 40px; line-height: 1; letter-spacing: -1px;
    background: linear-gradient(180deg, #ffffff 0%, #bdbdbd 45%, #6e6e6e 55%, #e0e0e0 100%);
    -webkit-background-clip: text; background-clip: text; color: transparent;
  }
  .headline-1 { left: 98px; top: 305px; }
  .headline-2 { left: 98px; top: 350px; font-size: 41px; }
  .script { left: 100px; top: 385px; font-family: "Mr Dafoe", cursive; font-size: 62px; color: var(--red-bright); line-height: 1; }
  .experience-band {
    left: 43px; top: 462px; width: 328px; height: 30px;
    background: linear-gradient(90deg, #c00000, var(--red) 70%);
    clip-path: polygon(0 0, 100% 0, 88% 100%, 0 100%);
    font-weight: 500; font-size: 23px; letter-spacing: 10px; padding-left: 18px; line-height: 30px;
  }

  /* Service cards */
  .service-card { top: 514px; width: 228px; height: 158px; border-radius: 12px; padding: 12px 12px 0 16px; }
  .service-card.red { background: linear-gradient(180deg, var(--red) 0%, #a80000 100%); color: var(--white); }
  .service-card.light { background: linear-gradient(180deg, #f2f2f2, #cfcfcf); color: var(--ink); }
  .card-head { display: flex; align-items: center; gap: 12px; height: 30px; margin-bottom: 6px; }
  .card-icon { width: 22px; height: 22px; flex: none; }
  .card-title { font-family: "Kanit", sans-serif; font-style: italic; font-weight: 800; font-size: 9.5px; line-height: 1.1; text-transform: uppercase; }
  .light .card-title { color: var(--red); }
  .service-list { list-style: none; font-size: 10.5px; line-height: 1.2; }
  .service-list li { position: relative; padding-left: 18px; margin-bottom: 5px; }
  .service-list li::before {
    content: ""; position: absolute; left: 2px; top: 2px; width: 7px; height: 7px; border-radius: 50%;
    background: currentColor; opacity: .85;
  }

  .extras-strip {
    left: 176px; top: 681px; width: 568px; height: 30px; border-radius: 8px;
    background: linear-gradient(180deg, #f4f4f4, #cdcdcd); color: var(--ink);
    display: flex; align-items: center; font-size: 11px;
  }
  .extras-strip .lead { font-family: "Kanit", sans-serif; font-style: italic; font-weight: 800; font-size: 10px; text-transform: uppercase; padding-left: 10px; display: flex; align-items: center; gap: 8px; width: 270px; }
  .extras-strip .item { display: flex; align-items: center; gap: 6px; padding: 0 16px; }
  .extras-strip .item + .item { border-left: 1px solid #9a9a9a; height: 22px; padding-left: 28px; }
  .tick { width: 7px; height: 7px; border-radius: 50%; background: var(--ink); }

  .factors-heading { left: 0; top: 720px; width: 920px; text-align: center; font-family: "Kanit", sans-serif; font-style: italic; font-weight: 800; font-size: 15.5px; text-transform: uppercase; }

  /* Factor columns */
  .factor {
    top: 768px; width: 146px; height: 222px; border: 1.5px solid var(--red); border-radius: 12px;
    text-align: center; padding: 32px 6px 0;
    font-family: "Roboto", sans-serif; font-size: 10.2px; line-height: 1.14;
  }
  .factor-title { font-family: "Oswald", sans-serif; font-weight: 500; font-style: italic; color: var(--red-bright); font-size: 11px; line-height: 1.2; margin-bottom: 6px; text-transform: uppercase; letter-spacing: -.2px; }
  .factor-hex { position: absolute; left: 50%; top: -22px; transform: translateX(-50%); width: 46px; height: 44px; }

  .closing { left: 41px; top: 1001px; width: 365px; font-size: 10px; line-height: 1.2; }
  .mobile { left: 476px; top: 999px; font-family: "Oswald", sans-serif; font-weight: 700; font-size: 28px; letter-spacing: -.5px; transform: skewX(-4deg); white-space: nowrap; }
  .mobile em { font-style: normal; color: var(--red-bright); }

  .visit-band { left: 0; top: 1048px; width: 920px; height: 32px; }
  .visit-label { left: 41px; top: 1049px; width: 330px; height: 22px; background: var(--white); color: var(--ink); font-size: 18px; letter-spacing: 7px; line-height: 22px; padding-left: 20px; clip-path: polygon(0 0, 94% 0, 100% 100%, 0 100%); }
  .address-bar { left: 364px; top: 1047px; width: 457px; height: 31px; background: linear-gradient(90deg, #b30000, var(--red) 50%, #c00000); clip-path: polygon(7% 0, 100% 0, 100% 100%, 0 100%); display: flex; align-items: center; gap: 16px; padding-left: 64px; font-size: 18px; font-weight: 500; }
  .pin { width: 14px; height: 20px; }
</style>
</head>
<body>
<main class="flyer">

  <svg class="abs hero-rings" viewBox="0 0 920 520" aria-hidden="false">
    <defs>
      <radialGradient id="photoTone" cx="55%" cy="60%" r="70%">
        <stop offset="0" stop-color="#c8321a"/>
        <stop offset=".35" stop-color="#7a1c14"/>
        <stop offset=".7" stop-color="#3b3b3b"/>
        <stop offset="1" stop-color="#8a8a8a"/>
      </radialGradient>
      <linearGradient id="silverRing" x1="0" y1="0" x2="1" y2="1">
        <stop offset="0" stop-color="#f0f0f0"/><stop offset=".5" stop-color="#8c8c8c"/><stop offset="1" stop-color="#dcdcdc"/>
      </linearGradient>
    </defs>
    <circle cx="718" cy="212" r="290" fill="url(#silverRing)"/>
    <circle cx="718" cy="212" r="282" fill="#000"/>
    <circle cx="718" cy="212" r="276" fill="#c20a0a"/>
    <circle cx="718" cy="212" r="266" fill="#000"/>
    <circle cx="718" cy="212" r="262" fill="url(#photoTone)" role="img" aria-label="Photo of a glossy red sports coupe parked on a city street"/>
  </svg>

  <div class="abs brand">
    <span class="brand-dot"></span>
    <span class="brand-name">Lumen 7 Auto Detail</span>
  </div>

  <p class="abs kicker">PROVIDING A</p>
  <h1 class="abs headline headline-1">UNIQUE &amp;</h1>
  <p class="abs headline headline-2">EXCEPTIONAL</p>
  <p class="abs script">Auto Detail</p>
  <p class="abs experience-band">EXPERIENCE</p>

  <section class="abs service-card red" style="left:44px">
    <div class="card-head">
      <svg class="card-icon" viewBox="0 0 24 24"><rect x="3" y="10" width="18" height="7" rx="2" fill="#fff"/><path d="M6 10l2-4h8l2 4z" fill="#fff"/><circle cx="7" cy="18" r="2" fill="#fff"/><circle cx="17" cy="18" r="2" fill="#fff"/></svg>
      <h2 class="card-title">Hand Wash</h2>
    </div>
    <ul class="service-list">
      <li>Clay Bar Application</li>
      <li>Machine Buff Wax /Compound / Polish Paint Correction</li>
      <li>Clean Interior &amp; Exterior Glass</li>
      <li>Vacuum, Shampoo, &amp; Steam Clean</li>
    </ul>
  </section>

  <section class="abs service-card light" style="left:346px">
    <div class="card-head">
      <svg class="card-icon" viewBox="0 0 24 24"><rect x="5" y="4" width="12" height="16" rx="2" fill="#e01010"/><rect x="8" y="8" width="6" height="2" fill="#fff"/></svg>
      <h2 class="card-title">Upholstery, Carpets,<br>Seats, Mats, &amp; Trunk</h2>
    </div>
    <ul class="service-list">
      <li>Pet Hair Removal</li>
      <li>Clean headliner</li>
      <li>Clean Doors/ Trunk/Hood Jambs</li>
      <li>Air Blow &amp; Clean all Cracks &amp; Crevices</li>
      <li>Clean &amp; Shine Protect All Vinyl/ Dash/Door Panels/Middle Console</li>
    </ul>
  </section>

  <section class="abs service-card red" style="left:647px">
    <div class="card-head">
      <svg class="card-icon" viewBox="0 0 24 24"><rect x="3" y="11" width="18" height="7" rx="2" fill="#fff"/><path d="M6 11l2-4h8l2 4z" fill="#fff"/><circle cx="7" cy="3" r="1.5" fill="#fff"/><circle cx="11" cy="4" r="1.5" fill="#fff"/></svg>
      <h2 class="card-title">Cleaning/Conditioning<br>of Leather</h2>
    </div>
    <ul class="service-list">
      <li>Clean, Treat, Dress, &amp; Polish Tires, Rims, &amp; Wheel Wells</li>
      <li>Bug &amp; Tar Removal</li>
      <li>Dress Black Exterior Plastic</li>
      <li>Minor Scratch Removal</li>
      <li>Engine Compartment Detail</li>
    </ul>
  </section>

  <div class="abs extras-strip">
    <span class="lead">
      <svg class="card-icon" viewBox="0 0 24 24" style="width:18px;height:18px"><rect x="3" y="9" width="18" height="8" rx="2" fill="#e01010"/><circle cx="8" cy="13" r="2" fill="#fff"/></svg>
      Headlight Restoration (if needed)
    </span>
    <span class="item"><span class="tick"></span>Interior Fragrance</span>
    <span class="item"><span class="tick"></span>DRY ICE BLASTING</span>
  </div>

  <h2 class="abs factors-heading">Here are a few key factors that make us stand out</h2>

  <article class="abs factor" style="left:42px">
    <svg class="factor-hex" viewBox="0 0 46 44"><polygon points="12,1 34,1 45,22 34,43 12,43 1,22" fill="#000" stroke="#e01010" stroke-width="2"/><rect x="12" y="20" width="18" height="7" rx="2" fill="#fff"/><path d="M15 20l2-4h8l2 4z" fill="#fff"/></svg>
    <h3 class="factor-title">Attention to Detail</h3>
    <p>We live up to our name by going above and beyond in every aspect of our car detailing services. Our team of skilled technicians pays meticulous attention to every nook and cranny of your vehicle, ensuring that it receives the highest level of care and precision</p>
  </article>
  <article class="abs factor" style="left:187px">
    <svg class="factor-hex" viewBox="0 0 46 44"><polygon points="12,1 34,1 45,22 34,43 12,43 1,22" fill="#000" stroke="#e01010" stroke-width="2"/><rect x="17" y="20" width="16" height="7" rx="2" fill="#fff"/><circle cx="12" cy="19" r="3" fill="#fff"/></svg>
    <h3 class="factor-title">Customized Solutions</h3>
    <p>We understand that each car is unique, and so are our clients' needs. That's why we offer personalized solutions tailored to your specific requirements. Whether you need a basic wash and wax or a comprehensive paint correction, we will work with you to create a customized detailing plan that meets your expectations</p>
  </article>
  <article class="abs factor" style="left:332px">
    <svg class="factor-hex" viewBox="0 0 46 44"><polygon points="12,1 34,1 45,22 34,43 12,43 1,22" fill="#000" stroke="#e01010" stroke-width="2"/><rect x="17" y="20" width="16" height="8" rx="2" fill="#fff"/><rect x="11" y="15" width="3" height="12" fill="#fff"/></svg>
    <h3 class="factor-title">Cutting-Edge Technology</h3>
    <p>We stay at the forefront of the industry by utilizing the latest tools, products, and techniques. Our team is trained in the most advanced detailing methods, allowing us to achieve superior results and deliver a finish that exceeds your expectations</p>
  </article>
  <article class="abs factor" style="left:477px">
    <svg class="factor-hex" viewBox="0 0 46 44"><polygon points="12,1 34,1 45,22 34,43 12,43 1,22" fill="#000" stroke="#e01010" stroke-width="2"/><circle cx="17" cy="15" r="2.5" fill="#fff"/><circle cx="23" cy="13" r="2.5" fill="#fff"/><circle cx="29" cy="15" r="2.5" fill="#fff"/><path d="M12 27q11 6 22-4" stroke="#fff" stroke-width="3" fill="none"/></svg>
    <h3 class="factor-title">Exceptional Customer<br>Service</h3>
    <p>We believe in providing not only exceptional car detailing but also an exceptional customer experience. Our friendly and knowledgeable staff is always ready to assist you, answer your questions, and ensure that you have a positive and enjoyable experience at our facility</p>
  </article>
  <article class="abs factor" style="left:622px; width:146px">
    <svg class="factor-hex" viewBox="0 0 46 44"><polygon points="12,1 34,1 45,22 34,43 12,43 1,22" fill="#000" stroke="#e01010" stroke-width="2"/><rect x="15" y="17" width="8" height="12" fill="#fff"/><rect x="25" y="21" width="6" height="8" fill="#fff"/><path d="M13 14a12 12 0 0 1 20 0" stroke="#fff" stroke-width="2" fill="none"/></svg>
    <h3 class="factor-title">Eco-Friendly Practices</h3>
    <p>We are committed to reducing our environmental impact by using eco-friendly cleaning products and techniques. Our detailing processes are designed to minimize water usage and waste generation, making us a responsible choice for those who care about the planet</p>
  </article>

  <p class="abs closing">These factors, combined with our passion for cars and dedication to excellence, make Lumen 7 Auto Detail the premier choice for discerning car owners who seek a truly exceptional detailing experience.</p>
  <p class="abs mobile">WE OFFER <em>MOBILE SERVICES</em> AS WELL</p>

  <p class="abs visit-label">VISIT OUR STORE</p>
  <p class="abs address-bar">
    <svg class="pin" viewBox="0 0 14 20"><path d="M7 0a7 7 0 0 1 7 7c0 5-7 13-7 13S0 12 0 7a7 7 0 0 1 7-7z" fill="#fff"/><circle cx="7" cy="7" r="2.6" fill="#c00000"/></svg>
    742 Corliss Ave. S., Renton, WA 98061
  </p>
</main>
</body>
</html>
```